Business Card Design for Tax Accounting Company

I need design files that can be edited to add new professional designations onto the end of my name once complete. I need design files that can be edited for new employees. I also need the design files to be able to upload into CardNest for new orders. I've attached multiple logo files with varying file extensions to help with the design.
Please include the following contact information:
Marcus Tellan, CFP®, EA, CTC, CEPA
Founder & CEO
C (480) 517.3082
F (623) 389.5170
718 W Larkspur Ave
Mesa, AZ 85210
Updates
I need the business card to include the following contact info:
C: (480)517.3082
F: (623) 389.5170
mt@RidgewayLedgerGroup.com
www.MarcusRTellan.com
Address to be included is
718 W Larkspur Ave
Mesa, AZ 85210
Business Cards are double sided
Target Market(s)
Business owners $1M+ annual revenue, especially for the construction and technology industries
Industry/Entity Type
Accounting & Tax
Contact Information for Business Card
Contact information and logo
Look and feel
Each slider illustrates characteristics of the customer's brand and the style your logo design should communicate.

```html
<!DOCTYPE html>
<html lang="en">
<head>
<meta charset="utf-8">
<title>Ridgeway Ledger Group – Business Card</title>
<link href="https://fonts.googleapis.com/css2?family=Poppins:wght@300;400;600;700&display=swap" rel="stylesheet">
<style>
  :root {
    --canvas: #cfcfcf;
    --paper: #ffffff;
    --navy: #0b1f5c;
    --navy-deep: #061a55;
    --navy-light: #132c75;
    --crimson: #c20f32;
    --sun: #ffd400;
    --rule: #8a94b8;
  }
  * { box-sizing: border-box; margin: 0; padding: 0; }
  html, body {
    width: 720px; height: 1200px; overflow: hidden;
    background: var(--canvas);
    font-family: "Poppins", sans-serif;
  }
  .card {
    position: absolute; left: 50px;
    width: 620px; height: 354px;
    box-shadow: 0 4px 8px rgba(0,0,0,0.25);
    overflow: hidden;
  }
  /* Front */
  .card--front { top: 218px; background: var(--paper); }
  .name-tab {
    position: absolute; left: 0; top: 33px;
    width: 245px; height: 62px;
    background: var(--crimson);
    border-radius: 0 31px 31px 0;
    padding: 7px 0 0 38px;
    color: #fff;
  }
  .name-tab__name { font-weight: 700; font-size: 24px; line-height: 28px; white-space: nowrap; }
  .name-tab__name .surname { color: var(--sun); }
  .name-tab__creds { font-weight: 400; font-size: 14px; line-height: 20px; white-space: nowrap; }
  .name-tab__creds sup { font-size: 8px; line-height: 0; }
  .brand {
    position: absolute; left: 30px; top: 200px; width: 218px;
    display: flex; flex-direction: column; align-items: center; gap: 12px;
  }
  .brand__dot { width: 56px; height: 56px; border-radius: 50%; background: var(--crimson); }
  .brand__name {
    font-weight: 600; font-size: 17px; color: var(--navy); text-align: center; line-height: 22px;
    white-space: nowrap;
  }
  .divider {
    position: absolute; left: 270px; top: 174px;
    width: 1px; height: 141px; background: var(--navy);
  }
  .contact-list { position: absolute; left: 300px; top: 169px; list-style: none; }
  .contact-list li {
    display: flex; align-items: center; height: 28.4px;
    font-weight: 300; font-size: 15px; color: var(--navy);
    white-space: nowrap;
  }
  .contact-list svg { width: 14px; height: 14px; margin-right: 18px; fill: var(--navy); flex: none; }
  /* Back */
  .card--back {
    top: 628px;
    background: linear-gradient(135deg, var(--navy-light) 0%, var(--navy-deep) 45%, var(--navy) 100%);
  }
  .brand--back { left: 0; top: 80px; width: 620px; }
  .brand--back .brand__dot { width: 64px; height: 64px; background: var(--sun); }
  .brand--back .brand__name { color: #fff; font-size: 22px; }
  .site-line {
    position: absolute; left: 0; right: 0; top: 308px;
    display: flex; align-items: center; gap: 12px;
    color: #fff; font-weight: 300; font-size: 18px; white-space: nowrap;
  }
  .site-line::before, .site-line::after {
    content: ""; flex: 1; height: 1px; background: var(--rule);
  }
</style>
</head>
<body>

<section class="card card--front">
  <div class="name-tab">
    <div class="name-tab__name">Marcus <span class="surname">Tellan</span></div>
    <div class="name-tab__creds">CFP<sup>®</sup>, EA, CTC, CEPA</div>
  </div>

  <div class="brand">
    <span class="brand__dot"></span>
    <span class="brand__name">Ridgeway Ledger Group</span>
  </div>

  <div class="divider"></div>

  <ul class="contact-list">
    <li>
      <svg viewBox="0 0 16 16"><path d="M3.5 1l2.5 0.5 1 3-1.6 1.2c0.8 1.8 2.2 3.2 4 4l1.2-1.6 3 1 0.4 2.5c0 0.8-0.6 1.4-1.4 1.4C6.8 13 3 9.2 2.1 2.4 2.1 1.6 2.7 1 3.5 1z"/></svg>
      480 517 3082
    </li>
    <li>
      <svg viewBox="0 0 16 16"><circle cx="8" cy="8" r="7"/><path d="M5 4c1 1 0 2 1 3s2 0 2 2-1 2 0 4" stroke="#fff" stroke-width="1.4" fill="none"/></svg>
      www.MarcusRTellan.com
    </li>
    <li>
      <svg viewBox="0 0 16 16"><rect x="1" y="5" width="3" height="10"/><rect x="5" y="3" width="10" height="12"/><rect x="7" y="5" width="6" height="2" fill="#fff"/><rect x="7" y="9" width="2" height="2" fill="#fff"/><rect x="11" y="9" width="2" height="2" fill="#fff"/><rect x="7" y="12" width="2" height="2" fill="#fff"/><rect x="11" y="12" width="2" height="2" fill="#fff"/></svg>
      623 389 5170
    </li>
    <li>
      <svg viewBox="0 0 16 16"><path d="M1 3h14v1.5L8 9 1 4.5z"/><path d="M1 6.3l7 4.5 7-4.5V13H1z"/></svg>
      mt@RidgewayLedgerGroup.com
    </li>
    <li>
      <svg viewBox="0 0 16 16"><path d="M8 0.5a5 5 0 0 1 5 5c0 3.5-5 10-5 10s-5-6.5-5-10a5 5 0 0 1 5-5z"/><circle cx="8" cy="5.5" r="2" fill="#fff"/></svg>
      718 W Larkspur Ave Mesa, AZ, 85210
    </li>
  </ul>
</section>

<section class="card card--back">
  <div class="brand brand--back">
    <span class="brand__dot"></span>
    <span class="brand__name">Ridgeway Ledger Group</span>
  </div>
  <div class="site-line">www.MarcusRTellan.com</div>
</section>

</body>
</html>
```